Need a business card for a Construction and Remodeling company.
Our company logo is the fleur de lis design as thats the family crust that we use on our logos.
Heres the info it needs:

Brackmore Construction & Remodeling, LLC
Renovations * Restorations

Elwin R. Brackmore
845 North Quarry Road
Ashgrove Vermont 05998
(203) 555.0182
CT LIC/REG: 418257

home owners, customers

```html
<!DOCTYPE html>
<html lang="en">
<head>
<meta charset="utf-8">
<title>Brackmore Construction &amp; Remodeling — Business Card</title>
<link rel="stylesheet" href="https://fonts.googleapis.com/css2?family=EB+Garamond:wght@400;500&family=Poppins:wght@300;400;600;700&display=swap">
<style>
  :root {
    --page-bg: #e9eaec;
    --band-blue: #1a5fb4;
    --brand-blue: #1d57a8;
    --card-grey: #b7b8ba;
    --card-grey-light: #c6c7c9;
    --card-white: #ffffff;
    --ink: #2b2b2b;
    --tagline: #ffffff;
  }
  html, body {
    margin: 0;
    width: 1200px;
    height: 1200px;
    overflow: hidden;
    background: var(--page-bg);
  }
  .business-card {
    position: absolute;
    left: 300px;
    top: 75px;
    width: 600px;
    height: 1050px;
    background: linear-gradient(to bottom, var(--card-grey) 0%, var(--card-grey-light) 48%, var(--card-white) 68%, var(--card-white) 100%);
    box-shadow: 0 10px 30px rgba(0,0,0,0.18);
    overflow: hidden;
  }
  .side-band {
    position: absolute;
    top: 0;
    bottom: 0;
    width: 52px;
    background: var(--band-blue);
  }
  .side-band--left { left: 0; }
  .side-band--right { right: 0; }
  .card-content {
    position: absolute;
    left: 52px;
    right: 52px;
    top: 0;
    bottom: 0;
    text-align: center;
  }
  .tagline {
    margin: 40px 0 0;
    font-family: "EB Garamond", Georgia, serif;
    font-size: 26px;
    letter-spacing: 1px;
    word-spacing: 12px;
    color: var(--tagline);
  }
  .brand {
    margin-top: 70px;
    display: flex;
    flex-direction: column;
    align-items: center;
    color: var(--brand-blue);
    font-family: "EB Garamond", Georgia, serif;
    font-weight: 500;
  }
  .brand-mark {
    width: 150px;
    height: 150px;
    border-radius: 50%;
    background: var(--brand-blue);
    margin-bottom: 40px;
  }
  .brand-name {
    font-size: 74px;
    line-height: 1;
    letter-spacing: 2px;
    text-transform: uppercase;
  }
  .brand-sub {
    margin-top: 8px;
    font-size: 20px;
    letter-spacing: 1.5px;
    text-transform: uppercase;
  }
  .contact {
    margin-top: 90px;
    font-family: "Poppins", Arial, sans-serif;
    color: var(--ink);
  }
  .contact-name {
    margin: 0 0 4px;
    font-size: 40px;
    font-weight: 700;
    line-height: 1.2;
  }
  .contact-line {
    margin: 0;
    font-size: 32px;
    font-weight: 300;
    line-height: 1.25;
  }
  .licence {
    margin: 30px 0 0;
    font-size: 22px;
    font-weight: 400;
    letter-spacing: 1px;
  }
</style>
</head>
<body>
  <div class="business-card">
    <div class="side-band side-band--left"></div>
    <div class="side-band side-band--right"></div>
    <div class="card-content">
      <p class="tagline">Renovations Additions Restorations</p>
      <div class="brand">
        <div class="brand-mark"></div>
        <div class="brand-name">Brackmore</div>
        <div class="brand-sub">Construction &amp; Remodeling, LLC</div>
      </div>
      <div class="contact">
        <p class="contact-name">Elwin R. Brackmore</p>
        <p class="contact-line">845 North Quarry Road</p>
        <p class="contact-line">Ashgrove</p>
        <p class="contact-line">Vermont 05998</p>
        <p class="contact-line">(203) 555.0182</p>
        <p class="licence">LIC/REG: 418257</p>
      </div>
    </div>
  </div>
</body>
</html>
```